New business card for my lawn and landscape business

Dorrin Yard and Building is a full-service lawn care, landscaping, and light construction company serving Paragould and the Northeast Arkansas region. The business is owned and operated by Marcus Toller, with a reputation for hands-on, detail-oriented service, dependable crews, and quality results for both residential and commercial clients. A well regarded business with great reviews.
Owner Marcus Toller
Dorrinyardandbuilding.example

Target Market(s)

Commercial, Middle, and upper class in north east Arkansas

Industry/Entity Type

Lawn maintenance and landscape

Contact Information for Business Card

Dorrin Yard And Building Professional lawn care, landscaping, and property improvement in Northeast Arkansas. • lawn maintenance •lawn treatments and weed control • exterior projects • Custom landscape design & installation • Sod, trees, rock & drainage solutions • Residential & commercial services Reliable. Detailed. Done right.

Requirements
Must have
• Business name, service area, list of some of our services, clean design that represents
Nice to have
• Unique. Different design element than just grass because its already in n the logo. Picture of a warm season (south) lawn or landscape. Pictures of the type of work we do

```html
<!DOCTYPE html>
<html lang="en">
<head>
<meta charset="UTF-8">
<title>Dorrin Yard and Building – Business Card</title>
<link href="https://fonts.googleapis.com/css2?family=Arimo:wght@400;700&display=swap" rel="stylesheet">
<style>
  :root {
    --bg: #e4e4e4;
    --card-white: #ffffff;
    --green: #72ad3e;
    --green-card: #7fb44a;
    --green-card-dark: #74ab41;
    --green-mark: #a9d27b;
    --ink: #4a4a4a;
    --rule: #c9c9c9;
    --white: #ffffff;
  }
  * { box-sizing: border-box; margin: 0; padding: 0; }
  html, body { width: 1200px; height: 1200px; overflow: hidden; }
  body {
    background: var(--bg);
    font-family: "Arimo", Arial, sans-serif;
    position: relative;
  }
  .card {
    position: absolute;
    width: 688px;
    height: 394px;
    border-radius: 18px;
    overflow: hidden;
  }
  .card--front { left: 267px; top: 159px; background: var(--card-white); }
  .card--back {
    left: 262px; top: 653px;
    background: linear-gradient(180deg, var(--green-card) 0%, var(--green-card-dark) 100%);
    color: var(--white);
  }

  /* brand lockup */
  .brand {
    position: absolute;
    display: flex;
    align-items: center;
    gap: 14px;
  }
  .brand__dot { flex: none; border-radius: 50%; }
  .brand__name { font-weight: 700; line-height: 1.1; }
  .card--front .brand { left: 410px; top: 70px; width: 240px; }
  .card--front .brand__dot { width: 46px; height: 46px; background: var(--green); }
  .card--front .brand__name { color: var(--green); font-size: 25px; }
  .card--back .brand { left: 70px; top: 140px; width: 240px; }
  .card--back .brand__dot { width: 46px; height: 46px; background: var(--green-mark); }
  .card--back .brand__name { color: var(--green-mark); font-size: 25px; }

  /* front details */
  .person { position: absolute; left: 48px; top: 211px; }
  .person__name { font-size: 27px; font-weight: 700; color: var(--green); letter-spacing: 0.2px; }
  .person__role { font-size: 15.5px; color: var(--ink); margin-top: 4px; }
  .rule { position: absolute; left: 48px; width: 593px; top: 280px; height: 1px; background: var(--rule); }
  .contacts { position: absolute; left: 46px; top: 291px; list-style: none; }
  .contacts li { display: flex; align-items: center; gap: 8px; font-size: 16px; color: var(--ink); height: 20.5px; }
  .contacts svg { width: 14px; height: 14px; flex: none; }

  /* back details */
  .about { position: absolute; left: 348px; top: 74px; width: 320px; }
  .about__intro { font-size: 15.5px; font-weight: 700; line-height: 19px; }
  .services { list-style: none; margin-top: 9px; }
  .services li { font-size: 15.5px; line-height: 23.2px; }
  .services li::before { content: "• "; }
  .tagline { font-size: 15.5px; font-weight: 700; margin-top: 12px; letter-spacing: 0.2px; }
</style>
</head>
<body>
  <section class="card card--front" aria-label="Card front">
    <div class="brand">
      <span class="brand__dot"></span>
      <span class="brand__name">Dorrin Yard and Building</span>
    </div>
    <div class="person">
      <h1 class="person__name">MARCUS TOLLER</h1>
      <p class="person__role">Owner</p>
    </div>
    <div class="rule"></div>
    <ul class="contacts">
      <li>
        <svg viewBox="0 0 24 24" aria-hidden="true"><path fill="#72ad3e" d="M6.6 10.8a15 15 0 0 0 6.6 6.6l2.2-2.2c.3-.3.7-.4 1-.2 1.1.4 2.3.6 3.6.6.6 0 1 .4 1 1V20c0 .6-.4 1-1 1A17 17 0 0 1 3 4c0-.6.4-1 1-1h3.5c.6 0 1 .4 1 1 0 1.3.2 2.5.6 3.6.1.3 0 .7-.2 1z"/></svg>
        555-014-2290
      </li>
      <li>
        <svg viewBox="0 0 24 24" aria-hidden="true"><rect x="2" y="5" width="20" height="14" rx="1" fill="#72ad3e"/><path d="M2.5 5.5 12 13l9.5-7.5" fill="none" stroke="#fff" stroke-width="1.6"/></svg>
        info@Dorrinyardandbuilding.example
      </li>
      <li>
        <svg viewBox="0 0 24 24" aria-hidden="true"><circle cx="12" cy="12" r="10" fill="#72ad3e"/><path d="M7 7c2 0 3 1 3 3s2 2 2 4-1 3-1 5M14 4c0 2 1 3 3 3s2 2 3 3" fill="none" stroke="#fff" stroke-width="1.6"/></svg>
        www.Dorrinyardandbuilding.example
      </li>
    </ul>
  </section>

  <section class="card card--back" aria-label="Card back">
    <div class="brand">
      <span class="brand__dot"></span>
      <span class="brand__name">Dorrin Yard and Building</span>
    </div>
    <div class="about">
      <p class="about__intro">Dorrin Yard &amp; Building<br>Professional lawn care, landscaping<br>&amp; property improvement in<br>Northeast Arkansas.</p>
      <ul class="services">
        <li>Lawn maintenance</li>
        <li>Lawn treatments &amp; weed control</li>
        <li>Exterior projects</li>
        <li>Custom landscape design &amp; installation</li>
        <li>Sod, trees, rock &amp; drainage solutions</li>
        <li>Residential &amp; commercial services</li>
      </ul>
      <p class="tagline">RELIABLE. DETAILED. DONE RIGHT</p>
    </div>
  </section>
</body>
</html>
```